Flyer Personenführungsanlage
Zielgruppe
Unser Unternehmen bietet Kommunikationslösungen rund um Veranstaltungen, Events und Messen an. Für Vorführungen auf Messen, Werksführungen und Dolmetscheraufgaben bieten wir sogenannte "Personenführungsanlagen" zur Miete an. Diese Anlagen bestehen aus einem Handmikrofon oder einem Headset, die Zuhörer erhalten einen Taschenempfänger mit Ohrhörer. Unsere Zielgruppe sind Eventagenturen, Veranstaltungstechnikfirmen, Kirchen, Schwerhörige, sowie Cityguides und Veranstalter.
Aufgabenstellung
Wir möchten für die Personenführungsanlage einen eigenen Produktflyer (max. 4 Seiten) im DIN lang Format 10,5cm x 21,0 cm entwickeln lassen. Alle Informationen und Texte zu diesen Produkten sind auf unserer Webseite. Der Flyer soll die auf der Einführungseite den Anwendungszweck von Personenführungsanlagen erklären, im Anschluss die Produkte Handsender KV-5, Taschenempfänger ZL-3, Ohrhörer MF-4,Kopfhörer MF-6, Induktionsschleife WE-700 sowie den Koffer B72 darstellen, und am Schluss die Einsatzgebiete des Systems (Besichtigungen,Dolmetschertechnik,Hörunterstützung,Effektives Training und Live Kommentare).

```html
<!DOCTYPE html>
<html lang="de">
<head>
<meta charset="utf-8">
<title>Flyer Personenführungsanlage</title>
<link href="https://fonts.googleapis.com/css2?family=PT+Sans+Narrow:wght@400;700&family=Open+Sans:wght@400;700&display=swap" rel="stylesheet">
<style>
:root{
  --teal:#1b87a4;
  --dark:#231f20;
  --grey:#d3d4d6;
  --grey-mid:#8e9093;
  --white:#ffffff;
  --bg:#eceded;
  --ink:#2b2b2b;
}
*{margin:0;padding:0;box-sizing:border-box}
html,body{width:1200px;height:742px;overflow:hidden;background:var(--bg)}
body{position:relative;font-family:"Open Sans",sans-serif;color:var(--ink)}
.head{font-family:"PT Sans Narrow",sans-serif;font-weight:700}
.panel{position:absolute;top:126px;height:490px;box-shadow:0 2px 8px rgba(0,0,0,.18);overflow:hidden}
.photo{position:absolute}

/* Cover */
.cover{left:40px;width:230px;background:var(--white)}
.brand{position:absolute;right:18px;top:40px}
.brand-name{display:flex;align-items:center;justify-content:flex-end;gap:5px;font-family:"Open Sans",sans-serif;font-weight:700;font-size:20px;color:var(--teal);letter-spacing:.5px}
.brand-dot{width:7px;height:7px;border-radius:50%;background:var(--teal)}
.cover-photo{left:0;top:146px;width:230px;height:143px;background:linear-gradient(135deg,#d9c7a8 0%,#b9a58a 45%,#5a5048 100%)}
.cover-base{position:absolute;left:0;top:289px;width:230px;height:201px;background:var(--teal)}
.cover-title{position:absolute;left:12px;top:22px;color:var(--white);font-size:19px}

/* Back panel */
.back{left:290px;width:250px;background:var(--white)}
.back-top{position:absolute;left:0;top:0;width:250px;height:142px;background:var(--teal)}
.back-title{position:absolute;left:12px;top:9px;color:var(--white);font-size:13px}
.uses{position:absolute;left:0;top:33px;width:240px;list-style:none}
.uses li{height:16px;margin-bottom:4.5px;background:var(--dark);border-radius:0 6px 6px 0;color:var(--white);font-family:"PT Sans Narrow",sans-serif;font-weight:700;font-size:7.2px;line-height:16px;padding-left:12px;white-space:nowrap}
.back-base{position:absolute;left:0;top:288px;width:250px;height:202px;background:var(--grey)}
.contact{position:absolute;left:24px;top:100px;font-family:"PT Sans Narrow",sans-serif;font-weight:700;font-size:6.4px;line-height:1.35;color:var(--dark)}
.contact p+p{margin-top:6px}
.contact-mark{position:absolute;left:0;top:100px;width:18px;height:24px;background:var(--white)}

/* Spread */
.spread{left:560px;width:600px;background:var(--grey)}
.page{position:absolute;top:0;width:300px;height:490px}
.page-left{left:0}
.page-right{left:300px;background:#c9cacc}
.band{position:absolute;left:0;width:300px;height:30px;background:var(--teal);color:var(--white);font-size:13px;padding:6px 0 0 16px}
.intro{position:absolute;left:0;top:30px;width:300px;height:172px;background:var(--white);padding:14px 14px 0 24px;font-size:6px;line-height:1.4;text-align:justify}
.intro p+p{margin-top:7px}
.intro-rule{position:absolute;left:6px;width:8px;background:var(--grey);z-index:1}
.box{position:absolute;padding:7px 8px;font-size:5.1px;line-height:1.4;text-align:justify}
.box h3{font-family:"PT Sans Narrow",sans-serif;font-weight:700;font-size:8.4px;margin-bottom:5px}
.box-white{background:var(--white)}
.box-teal{background:var(--teal);color:var(--white)}
.box-dark{background:var(--dark);color:var(--white)}
.box-grey{background:var(--grey-mid);color:var(--white)}
.right-title h3{text-align:right}
.teal-title h3{color:var(--teal)}
.prod-img{position:absolute;background:linear-gradient(160deg,#ffffff 30%,#cfd2d4 100%)}
.right-head{position:absolute;right:12px;top:8px;color:var(--white);font-size:13px}
</style>
</head>
<body>

<section class="panel cover" aria-label="Titelseite">
  <div class="brand">
    <div class="brand-name"><span class="brand-dot"></span>VENDARO</div>
  </div>
  <div class="photo cover-photo" role="img" aria-label="Foto: Referentin mit Handmikrofon, daneben Zuhörer mit Ohrhörern bei einer Führung"></div>
  <div class="cover-base">
    <h1 class="head cover-title">Personenführungsanlage</h1>
  </div>
</section>

<section class="panel back" aria-label="Rückseite">
  <div class="back-top">
    <h2 class="head back-title">Einsatzgebiete</h2>
    <ul class="uses">
      <li>Führungen / Besichtigungen</li>
      <li>Dolmetschersystem und mobile Flüsteranlage</li>
      <li>Schwerhörigenanlage zur Hörunterstützung in öffentlichen Einrichtungen</li>
      <li>Kommandoanlage für effektives Training</li>
      <li>Übertragungssystem für Live Kommentare für Sehbehinderte</li>
    </ul>
  </div>
  <div class="back-base">
    <div class="contact-mark"></div>
    <div class="contact">
      <p>VENDARO<br>Lindenweg 14<br>70563-Musterstadt</p>
      <p>Telefon: (0711) 48 22 90<br>Fax: (0711) 48 22 91</p>
      <p>www.vendaro-verleih.de</p>
    </div>
  </div>
</section>

<section class="panel spread" aria-label="Innenseiten">
  <div class="page page-left">
    <h2 class="head band" style="top:0">Führungsanlage</h2>
    <div class="intro">
      <p>Das gesprochene Wort ist bei der Übertragung von Informationen unerlässlich: Ob im kleinen Personenkreis oder innerhalb großer Gruppen. Egal ob bei Werks- oder Stadtführungen, Bus- oder Schiffsreisen, Dolmetscher- bzw. Hörunterstützung oder Trainings - die optimale Verständigung mit Ihren Gästen ist unerlässlich.</p>
      <p>Bei diesen Anforderungen werden zur Unterstützung sogenannte Führungsanlagen oder auch Flüsteranlagen eingesetzt.</p>
      <p>Es gibt zahlreiche Systeme von unterschiedlichsten Herstellern am Markt. Eines der modernsten Systeme auch in Punkto Zuverlässigkeit, Robustheit und Einfachheit in der Bedienung ist das Tour Guide System Tonara aus dem Hause Klangwerk.</p>
      <p>Wir vermieten das Klangwerk Tonara System - das grosse Spektrum der Anwendungsmöglichkeiten sowie die breite Auswahl an Zubehör haben uns von diesem System überzeugt.</p>
    </div>
    <div class="intro-rule" style="top:40px;height:70px"></div>
    <div class="intro-rule" style="top:118px;height:36px"></div>
    <div class="intro-rule" style="top:162px;height:32px"></div>
    <h2 class="head band" style="top:204px">Produkte</h2>

    <div class="prod-img" style="left:6px;top:246px;width:62px;height:108px" role="img" aria-label="Produktfoto: Handsender KV-5"></div>
    <div class="box box-white right-title teal-title" style="left:72px;top:246px;width:228px;height:108px;border-radius:10px 0 0 0">
      <h3>Handsender KV-5</h3>
      Der <b>Handsender KV-5</b> kann mit beliebig vielen Taschenempfängern ZL-3 eingesetzt werden. Die Reichweite des Handsenders beträgt ca. 100m bei Sichtverbindung. Der Sender bietet bis zu 18 unterschiedliche Frequenzen. Die Sendetaste unterhalb der Mikrofonkopfes kann vom Nutzer individuell als Schalter, Taster oder Mute-Funktion eingestellt werden. Das geräuschkompensierte Mikrofon verfügt über eine rückkopplungsarme Nierencharakteristik. Die Stromversorgung erfolgt über 2 handelsübliche AA-Batterien bzw. Akkus.
    </div>

    <div class="box box-teal" style="left:6px;top:362px;width:168px;height:112px;border-radius:0 0 12px 0">
      <h3>Taschenempfänger ZL-3</h3>
      Der leichte Empfänger kann bequem am Gürtel befestigt oder mit einer Trageschlaufe um den Hals getragen werden - die Reichweite beträgt ca. 100m bei Sichtverbindung. Wie bei den Sendern können bis 18 unterschiedliche Frequenzen ausgewählt werden. Die Lautstärke wird über einen Drehregler eingestellt. Als Kopfhörer stehen unterschiedliche Ohrhörer zur Auswahl. Alle Funktionen können über eine Sperrfunktion gegen versehentliches Verstellen gesperrt werden. Die Versorgung erfolgt über 2 AA-Akkus.
    </div>
    <div class="prod-img" style="left:178px;top:362px;width:122px;height:112px;border-radius:10px 0 0 0" role="img" aria-label="Produktfoto: Taschenempfänger ZL-3 mit Ohrhörer"></div>
  </div>

  <div class="page page-right">
    <h2 class="head right-head">Produkte</h2>
    <div class="prod-img" style="left:0;top:30px;width:72px;height:106px" role="img" aria-label="Produktfoto: Ohrhörer MF-4"></div>
    <div class="box box-teal right-title" style="left:76px;top:30px;width:224px;height:106px;border-radius:12px 0 0 0">
      <h3>Ohrhörer MF-4</h3>
      Der <b>Ohrhörer MF-4</b> wird zusammen mit dem <b>Taschenempfänger ZL-3</b> zum Einsatz. Für optimalen Tragekomfort sorgt der dehnbare Ohrbügel. Das für den Hörer verwendete Neodym-Magnetsystem sorgt für hervorragende Klangeigenschaften und beste Sprachverständlichkeit. Der Ohrhörer kann wahlweise links oder rechts getragen werden. Die Oberfläche des Ohrhörers kann leicht gereinigt werden und ist somit hygienisch einwandfrei für den nächsten Einsatz.
    </div>

    <div class="box box-white teal-title" style="left:0;top:142px;width:190px;height:94px;border-radius:0 0 10px 0">
      <h3>Kopfhörer MF-6</h3>
      Alternativ zum Ohrhörer kann der <b>Kopfhörer MF-6</b> eingesetzt werden. Der zweiseitige Kopfbügelhörer kann seitlich individuell auf den Kopf des Trägers eingestellt werden. Das Kabel zum Taschenempfänger ZL-3 hat eine Länge von 80cm. Die Schaumstoffüberzüge der Ohrhörer können nach Gebrauch leicht ausgetauscht werden und sorgen für maximale Hygiene.
    </div>
    <div class="prod-img" style="left:196px;top:142px;width:104px;height:94px;border-radius:10px 0 0 0" role="img" aria-label="Produktfoto: Kopfhörer MF-6"></div>

    <div class="prod-img" style="left:0;top:246px;width:96px;height:112px" role="img" aria-label="Produktfoto: Induktionsschleife WE-700"></div>
    <div class="box box-dark right-title" style="left:104px;top:246px;width:196px;height:112px;border-radius:12px 0 0 0">
      <h3>Induktionsschleife WE-700</h3>
      Mit der <b>Induktionsschleife WE-700</b> können Menschen mit Induktions-Hörgeräten ganz einfach eingebunden werden. Einfach die Induktionsschleife an den Taschenempfänger ZL-3 anschliessen, die Schleife um den Hals hängen und die Veranstaltung kann beginnen. Die Induktionsschleife wird von allen gängigen Induktions-Hörgeräten (z.B. Audivo) unterstützt.
    </div>

    <div class="box box-grey" style="left:0;top:362px;width:136px;height:112px;border-radius:0 0 12px 0">
      <h3>Lade-und Transportkoffer</h3>
      Die Tonara Führungsanlage liefern wir ab 10 Taschenempfänger im praktischen <b>Lade- und Transportkoffer</b>. Das integrierte Ladegerät bietet Platz für bis zu 20 Taschenempfängern sowie einem Handsender. Die seitlichen Fächer nehmen bis zu 40 Headsets bzw. Induktionsschleifen auf. Der Trolley im Reisekofferformat ist mit Rollen ausgestattet und kann bequem an den Einsatzort transportiert werden.
    </div>
    <div class="prod-img" style="left:142px;top:362px;width:158px;height:112px;border-radius:10px 0 0 0" role="img" aria-label="Produktfoto: Lade- und Transportkoffer mit Empfänger und Handsender"></div>
  </div>
</section>

</body>
</html>
```